Wordpress Web Design & Coding for velqorahealth.ca

We need a website for a new investment company that is visually grabbing and vibrant. We would like to see a web page that displays trust, growth and confidence. Needs to be responsive and mobile friendly for all browsers and coded for both Android & IOS.

Open to the number of pages and menu items. I selected 4 but if you feel the layout would work better with less I am open to this. Need to sell the people (management team/related businesses) and then show where the invested money will be going (upcoming projects).

Company Info:

Velq Ora is an investment company put together by a group of seasoned business professionals who have come together to combine decades of success in the real estate development, management, financing and medical services. The company will be a full service company offering turn key solutions for medical professionals.

Velq-Ora will focus on providing a full range of services via a group of distinct companies to deliver newly emerging needs of the medical community. The end goal will be to create complete solutions for individuals in the medical community. Our group has experience and success with the conceptualization, construction and financing of medical and dental clinic spaces. Velq-Ora Solutions will be established to accommodate all areas of the development and creation of clinics for medical professionals from building construction to equipment financing and administrations.

You can mention these companies and take photos from their websites. You can also use stock photos.

Our construction partner:
https://812bld.com/projects/

Our equipment leasing partner:
https://www.lomerix.com/

Our Management Team and medical partners

Dale Pickett
https://www.yourcalmpath.ca/

Milos Vandergrift
https://www.qhzdentalservices.com/about-us

PROPOSED PROJECTS (see attachment for details)
Harlow Ridge Business Park
Dunmere Business Park
Mt. Corwin Way Professional

Target Market(s)

Investors

Industry/Entity Type

Investment

Coding

Coded - Design and coding required

Number of Pages Required

4 page

Font styles to use
Sans Serif

Requirements
Must have
• Wordpress – must be both desktop and mobile friendly with fast page load speed
Ability to edit after ourselves in Wordpress
Attractive home page with logo etc.
Logo colours are: for the blue the pantone color is #0355a3
and for the green is #8cc63f

Sections, about us, what we do/services we provide, contact us

```html
<!DOCTYPE html>
<html lang="en">
<head>
<meta charset="utf-8">
<title>Velq-Ora Solutions</title>
<link href="https://fonts.googleapis.com/css2?family=Oswald:wght@300;400&family=Poppins:wght@400;500&display=swap" rel="stylesheet">
<style>
:root{
  --blue:#0355a3;
  --green:#8cc63f;
  --ink:#333;
  --grey:#f2f2f2;
  --white:#fff;
}
*{box-sizing:border-box;margin:0;padding:0}
html,body{width:1200px;height:3649px;overflow:hidden}
body{font-family:"Poppins",sans-serif;color:var(--ink);background:var(--white);position:relative}
a{color:inherit;text-decoration:none}
.abs{position:absolute}

/* header */
.topbar{top:0;left:0;width:1200px;height:54px}
.topbar .contact{position:absolute;top:16px;font-size:15px;color:var(--blue);display:flex;align-items:center;gap:8px}
.navbar{top:54px;left:496px;width:704px;height:48px;background:var(--blue)}
.navbar .tick{position:absolute;left:-4px;top:0}
.navbar a{position:absolute;top:13px;font-size:16px;color:var(--white)}
.navbar a.active{color:var(--green)}
.brand{top:0;left:142px;width:187px;height:130px;background:var(--white);box-shadow:0 4px 10px rgba(0,0,0,.18);display:flex;flex-direction:column;align-items:center;justify-content:center;z-index:3;clip-path:polygon(0 0,100% 0,100% 88%,50% 100%,0 88%)}
.brand span{font-size:24px;font-weight:500;color:var(--blue);line-height:1.15;text-align:center}

/* hero */
.hero{top:102px;left:0;width:1200px;height:512px;background:linear-gradient(180deg,#8fb8e0 0%,#c9dbea 45%,#9a9c98 75%,#6f7a62 100%)}
.hero h1{position:absolute;top:40px;left:0;width:1200px;text-align:center;font-family:"Oswald",sans-serif;font-weight:400;font-size:38px;line-height:47px;color:#1e1e1e}

/* shared */
.section-title{position:absolute;left:0;width:1200px;text-align:center;font-size:31px;font-weight:400;color:var(--blue)}
.section-title em{font-style:normal;color:var(--green)}
.rule{position:absolute;left:583px;width:34px;height:2px;background:#555}
.btn{position:absolute;height:32px;background:var(--blue);color:var(--white);font-size:15px;font-weight:500;display:flex;align-items:center;justify-content:center;padding-left:20px}
.btn svg{position:absolute;left:-14px;top:-4px}
.band-grey{left:0;width:1200px;background:linear-gradient(180deg,#f0f0f0,#f9f9f9 50%,#f0f0f0)}

/* solutions */
.service{position:absolute;width:282px}
.service .icon{width:75px;height:75px;border:2px solid var(--blue);border-radius:50%;display:flex;align-items:center;justify-content:center}
.service h3{margin-top:28px;font-size:18px;font-weight:500;color:var(--blue)}
.service p{margin-top:8px;font-size:13px;line-height:23px;color:#444}
.service .more{display:inline-block;margin-top:14px;font-size:14px;color:var(--green);border-bottom:1px solid var(--green)}
.solutions-art{top:808px;left:448px;width:289px;height:273px;background:linear-gradient(135deg,#2f6fb4,#5b93c9 50%,#8cc63f)}

/* about */
.about-text{position:absolute;top:1282px;left:160px;width:880px;text-align:center;font-size:13px;line-height:23px;color:#333}
.about-text p{margin-bottom:9px}

/* team */
.member{position:absolute;top:1700px;width:270px;height:316px;color:var(--white)}
.member .photo{position:absolute;left:0;bottom:0;width:150px;height:270px}
.member h4{position:absolute;top:96px;left:140px;width:126px;font-size:18px;font-weight:500;line-height:22px}
.member.blue{background:var(--blue)}
.member.blue .photo{background:linear-gradient(180deg,#2a6db0,#5a6a5a)}
.member.green{background:var(--green)}
.member.green .photo{background:linear-gradient(180deg,#a3d364,#7d8fb0)}
.partner-name{position:absolute;top:2028px;width:270px;text-align:center;font-size:30px;color:#222;letter-spacing:1px}
.partner-name.small{font-size:20px;color:#555}

/* projects */
.project{position:absolute;top:2315px;width:285px}
.project .shot{height:189px}
.project h4{margin-top:20px;font-size:15px;font-weight:400;color:#111}
.project p{margin-top:6px;font-size:11.5px;line-height:18px;color:#444}

/* partners */
.partner-title{position:absolute;top:2812px;font-size:24px;color:var(--blue);text-align:center;width:445px}
.partner-title em{font-style:normal;color:var(--green)}
.partner-box{position:absolute;top:2869px;height:114px;background:var(--white);box-shadow:0 2px 10px rgba(0,0,0,.15);display:flex;align-items:center;justify-content:center;font-size:24px;font-weight:500}

/* cta */
.cta-text{position:absolute;top:3124px;left:0;width:1200px;text-align:center;font-size:21px;line-height:34px;color:var(--blue)}
.cta-text em{font-style:normal;color:var(--green)}

/* footer */
.footer{top:3316px;left:0;width:1200px;height:290px;background:var(--blue);color:var(--white)}
.footer .fname{position:absolute;top:56px;left:0;width:1200px;text-align:center;font-size:26px;font-weight:500}
.footer nav a{position:absolute;top:170px;font-size:17px}
.footer nav a.active{color:var(--green)}
.footer .info{position:absolute;top:226px;display:flex;gap:12px;font-size:13px;line-height:18px}
.copy{top:3606px;left:0;width:1200px;height:43px;background:var(--green);color:var(--white);font-size:13px;display:flex;align-items:center;justify-content:center}
</style>
</head>
<body>

<!-- Header -->
<header>
  <div class="abs topbar">
    <span class="contact" style="left:705px">
      <svg width="20" height="20" viewBox="0 0 24 24" fill="none" stroke="#8cc63f" stroke-width="1.8"><path d="M5 3h4l2 5-2.5 1.5a11 11 0 0 0 6 6L16 13l5 2v4a2 2 0 0 1-2 2A17 17 0 0 1 3 5a2 2 0 0 1 2-2z"/></svg>
      604.555.0182
    </span>
    <span class="contact" style="left:862px">
      <svg width="20" height="20" viewBox="0 0 24 24" fill="none" stroke="#8cc63f" stroke-width="1.8"><rect x="3" y="6" width="18" height="13" rx="1"/><path d="M3 7l9 7 9-7"/></svg>
      inquiry@velqorahealth.ca
    </span>
  </div>
  <div class="abs brand"><span>Velq-Ora<br>Solutions</span></div>
  <nav class="abs navbar">
    <svg class="tick" width="60" height="48" viewBox="0 0 60 48"><path d="M-10 26l14 22L60 0H48L6 38z" fill="#8cc63f"/></svg>
    <a class="active" href="#" style="left:71px">Home</a>
    <a href="#" style="left:169px">About Us</a>
    <a href="#" style="left:297px">Our Solutions</a>
    <a href="#" style="left:458px">Contact Us</a>
  </nav>
</header>

<!-- Hero -->
<section class="abs hero" role="img" aria-label="Doctor with clipboard in front of a modern medical business park building">
  <h1>Velq-Ora Is An Investment Company That Focuses On Offering<br>Turn Key Solutions For Medical Professionals.</h1>
</section>

<!-- Solutions -->
<h2 class="section-title" style="top:708px">Our <em>Solutions</em></h2>
<div class="rule" style="top:760px"></div>

<div class="service" style="top:815px;left:143px">
  <div class="icon">
    <svg width="40" height="40" viewBox="0 0 40 40" fill="none" stroke="#0355a3" stroke-width="2"><rect x="8" y="6" width="20" height="28" rx="2"/><path d="M13 14h10M13 20h10M13 26h6"/><circle cx="29" cy="29" r="6" stroke="#8cc63f"/></svg>
  </div>
  <h3>Leasing Operations</h3>
  <p>Lorem ipsum dolor sit amet, consectetuer adipiscing elit, sed diam nonummy nibh euismod tincidunt ut laoreet dolore magna aliquam erat volutpat.</p>
  <a class="more" href="#">Read More</a>
</div>

<div class="abs solutions-art" role="img" aria-label="Photo collage of medical professionals at work"></div>

<div class="service" style="top:815px;left:769px">
  <div class="icon">
    <svg width="42" height="40" viewBox="0 0 42 40" fill="none" stroke="#0355a3" stroke-width="2"><rect x="5" y="10" width="32" height="22" rx="2"/><path d="M5 17h32"/><path d="M21 20l6 2v4c0 3-3 5-6 6-3-1-6-3-6-6v-4z" stroke="#8cc63f"/></svg>
  </div>
  <h3>Security Measures</h3>
  <p>Lorem ipsum dolor sit amet, consectetuer adipiscing elit, sed diam nonummy nibh euismod tincidunt ut laoreet dolore magna aliquam erat volutpat.</p>
  <a class="more" href="#">Read More</a>
</div>

<!-- About -->
<section class="abs band-grey" style="top:1152px;height:398px"></section>
<h2 class="section-title" style="top:1214px">About Velq-Ora <em>Solutions</em></h2>
<div class="rule" style="top:1265px"></div>
<div class="about-text">
  <p>Velq-Ora is an investment company put together by a group of seasoned business professionals who have come together to combine decades of success in the real estate development, management, financing and medical services. The company will be a full service company offering turn key solutions for medical professionals.</p>
  <p>Velq-Ora will focus on providing a full range of services via a group of distinct companies to deliver newly emerging needs of the medical community.</p>
  <p>The end goal will be to create complete solutions for individuals in the medical community.</p>
</div>
<a class="btn" href="#" style="top:1445px;left:533px;width:134px">
  <svg width="36" height="36" viewBox="0 0 36 36"><path d="M2 18l10 14L36 2h-6L12 24l-6-8z" fill="#8cc63f"/></svg>
  Read More
</a>

<!-- Team -->
<h2 class="section-title" style="top:1613px">Our Management <em>Team</em></h2>

<div class="member blue" style="left:142px">
  <div class="photo" role="img" aria-label="Portrait of Ned Holloway"></div>
  <h4>Ned Holloway</h4>
</div>
<div class="member green" style="left:465px">
  <div class="photo" role="img" aria-label="Portrait of Milos Vandergrift"></div>
  <h4>Milos Vandergrift</h4>
</div>
<div class="member blue" style="left:788px">
  <div class="photo" role="img" aria-label="Portrait of Dr. Dale Pickett"></div>
  <h4>Dr. Dale Pickett</h4>
</div>
<div class="partner-name" style="left:142px">calmpath</div>
<div class="partner-name small" style="left:465px;top:2034px">QHZ Dental Services Ltd.</div>
<div class="partner-name" style="left:788px">calmpath</div>

<!-- Projects -->
<section class="abs band-grey" style="top:2155px;height:591px"></section>
<h2 class="section-title" style="top:2233px">Upcoming <em>Projects</em></h2>

<div class="project" style="left:143px">
  <div class="shot" role="img" aria-label="Rendering of a single storey business park with tenant signs" style="background:linear-gradient(180deg,#6fa3dc,#c7ccd0 60%,#7b8670)"></div>
  <h4>Dunmere Business Park</h4>
  <p>Lorem ipsum dolor sit amet, consectet dipiscing elit, sed diam nonummy nibh euismod tincidunt ut laoreet dolore magna aliquam.</p>
</div>
<div class="project" style="left:458px">
  <div class="shot" role="img" aria-label="Interior of a professional clinic reception area" style="background:linear-gradient(180deg,#d9d4cc,#9c8a74 60%,#5b564f)"></div>
  <h4>Mt. Corwin Way Professional</h4>
  <p>Lorem ipsum dolor sit amet, consectet dipiscing elit, sed diam nonummy nibh euismod tincidunt ut laoreet dolore magna aliquam.</p>
</div>
<div class="project" style="left:772px">
  <div class="shot" role="img" aria-label="Three storey office building at dusk" style="background:linear-gradient(180deg,#a9c1e0,#c59a86 55%,#6b6c72)"></div>
  <h4>Dunmere Business Park - 2</h4>
  <p>Lorem ipsum dolor sit amet, consectet dipiscing elit, sed diam nonummy nibh euismod tincidunt ut laoreet dolore magna aliquam.</p>
</div>

<a class="btn" href="#" style="top:2636px;left:486px;width:228px">
  <svg width="36" height="36" viewBox="0 0 36 36"><path d="M2 18l10 14L36 2h-6L12 24l-6-8z" fill="#8cc63f"/></svg>
  Download&nbsp; Project PDF
</a>

<!-- Partners -->
<h3 class="partner-title" style="left:143px">Our Construction <em>Partner</em></h3>
<h3 class="partner-title" style="left:616px">Our Equipment <em>Leasing Partner</em></h3>
<div class="partner-box" style="left:143px;width:445px;color:#1f2f5c">812 Builders Inc.</div>
<div class="partner-box" style="left:616px;width:444px;color:#7a2a3a">Lomerix Equipment Leasing Inc.</div>

<!-- Call to action -->
<section class="abs band-grey" style="top:3053px;height:263px"></section>
<p class="cta-text">Velq-Ora Will Focus On Providing A Full Range of Services Via A Group of Distinct<br>Companies To <em>Deliver Newly Emerging Needs of The Medical Community.</em></p>
<a class="btn" href="#" style="top:3204px;left:507px;width:187px">
  <svg width="36" height="36" viewBox="0 0 36 36"><path d="M2 18l10 14L36 2h-6L12 24l-6-8z" fill="#8cc63f"/></svg>
  Contact Us Today
</a>

<!-- Footer -->
<footer class="abs footer">
  <div class="fname">Velq-Ora Solutions</div>
  <nav>
    <a class="active" href="#" style="left:360px">Home</a>
    <a href="#" style="left:464px">About Us</a>
    <a href="#" style="left:592px">Our Solutions</a>
    <a href="#" style="left:753px">Contact Us</a>
  </nav>
  <div class="info" style="left:210px">
    <svg width="18" height="22" viewBox="0 0 18 22"><path d="M9 1a7 7 0 0 0-7 7c0 5 7 13 7 13s7-8 7-13a7 7 0 0 0-7-7z" fill="#8cc63f"/><circle cx="9" cy="8" r="2.5" fill="#0355a3"/></svg>
    <span>Street Name, City Name<br>State Zipcode</span>
  </div>
  <div class="info" style="left:546px">
    <svg width="20" height="20" viewBox="0 0 24 24" fill="none" stroke="#8cc63f" stroke-width="1.8"><path d="M5 3h4l2 5-2.5 1.5a11 11 0 0 0 6 6L16 13l5 2v4a2 2 0 0 1-2 2A17 17 0 0 1 3 5a2 2 0 0 1 2-2z"/></svg>
    <span>Call Us<br>604.555.0147</span>
  </div>
  <div class="info" style="left:800px">
    <svg width="20" height="20" viewBox="0 0 24 24" fill="none" stroke="#8cc63f" stroke-width="1.8"><rect x="3" y="6" width="18" height="13" rx="1"/><path d="M3 7l9 7 9-7"/></svg>
    <span>Email Us<br>inquiry@velqorahealth.ca</span>
  </div>
</footer>
<div class="abs copy">Copyright © 2020 Velq-Ora Solutions. All Rights Reserved.</div>

</body>
</html>
```